Project Manager Business Card for Top Architectural Firm

Update and design a stunning Senior Project Manager Business Card

MARCO T. DRUMMOND II
Senior Project Manager

H A L C Y O N
A R C H I T E C T U R E L L C.
www.HalcyonGrandEstates.example
4127 NW 52nd Ter. Suite 2308
Miami, FL 33148
C: (305) 555-0184
mdrummond.halcyongrandestates@mailbox.example

Looking to have the logo to be UV Spot ink printed and to be prominent.

Target Market(s)

High end real estate architecture construction

Industry/Entity Type

Architect

Contact Information for Business Card

MARCO T. DRUMMOND II
Senior Project Manager

H A L C Y O N
Miami, FL 33148
C: (305) 555-0184

Font styles to use
Sans Serif

Colors

Designer to choose colors to be used in the design.

Requirements
Must have
• Prominent Logo

```html
<!DOCTYPE html>
<html lang="en">
<head>
<meta charset="utf-8">
<title>Halcyon Architecture LLC – Business Card</title>
<link rel="stylesheet" href="https://fonts.googleapis.com/css2?family=Antonio:wght@100;200&family=Oswald:wght@300;400&family=Source+Sans+3:wght@400&display=swap">
<style>
  :root {
    --stage: #424242;
    --card-light: #f3f3f3;
    --card-dark: #231f20;
    --ink: #1d1d1d;
    --blue: #2fa3dc;
    --blue-deep: #1f6f9c;
    --blue-soft: #7cc6ea;
    --coral: #e45a45;
    --white: #ffffff;
  }
  * { margin: 0; padding: 0; box-sizing: border-box; }
  html, body {
    width: 1200px; height: 900px; overflow: hidden;
    background: var(--stage);
  }
  .stage { position: relative; width: 1200px; height: 900px; }
  .card {
    position: absolute; top: 200px; width: 310px; height: 502px; overflow: hidden;
  }
  .card--front {
    left: 253px; background: var(--card-light);
    border-radius: 46px 0 46px 0;
  }
  .card--back {
    left: 627px; background: var(--card-dark);
    border-radius: 0 46px 0 46px;
  }
  .brand-dot {
    position: absolute; left: 118px; top: 46px; width: 74px; height: 74px;
    border-radius: 50%; background: var(--blue);
  }
  .wordmark {
    position: absolute; text-align: center; white-space: nowrap; line-height: 1;
  }
  .wordmark__name { font-family: "Antonio", sans-serif; font-weight: 100; }
  .wordmark__sub { font-family: "Oswald", sans-serif; font-weight: 300; }
  .card--front .wordmark { left: 35px; width: 240px; color: var(--ink); }
  .card--front .wordmark__name { top: 164px; font-size: 68px; letter-spacing: 3px; }
  .card--front .wordmark__sub { top: 237px; font-size: 10px; letter-spacing: 2.8px; }
  .contact {
    position: absolute; left: 21px; top: 282px; right: 12px;
    font-family: "Source Sans 3", sans-serif; color: var(--ink);
  }
  .contact__name {
    font-family: "Oswald", sans-serif; font-weight: 400; font-size: 18px;
    color: var(--blue); line-height: 24px;
  }
  .contact__title { font-size: 15px; color: var(--coral); line-height: 18px; margin-bottom: 8px; }
  .contact__address { font-size: 14px; line-height: 18px; }
  .contact__spaced { letter-spacing: 3.4px; }
  .contact__lines { list-style: none; margin-top: 13px; font-size: 14px; line-height: 19px; }
  .contact__lines li { display: flex; align-items: center; gap: 6px; white-space: nowrap; }
  .contact__lines .email { font-size: 11px; }
  .icon { width: 11px; height: 11px; flex: none; fill: var(--blue); }
  .back-band {
    position: absolute; left: 0; top: 0; width: 100%; height: 300px;
    background: linear-gradient(100deg, var(--blue-deep) 0%, var(--blue) 55%, var(--blue-soft) 100%);
  }
  .card--back .wordmark { left: 62px; width: 240px; color: var(--white); }
  .card--back .wordmark__name { top: 322px; font-size: 78px; letter-spacing: 3px; }
  .card--back .wordmark__sub { top: 405px; font-size: 11px; letter-spacing: 3px; }
</style>
</head>
<body>
<main class="stage">
  <section class="card card--front" aria-label="Business card front">
    <div class="brand-dot" aria-hidden="true"></div>
    <div class="wordmark wordmark__name">HALCYON</div>
    <div class="wordmark wordmark__sub">ARCHITECTURE LLC</div>
    <div class="contact">
      <p class="contact__name">MARCO T. DRUMMOND II</p>
      <p class="contact__title">Senior Project Manager</p>
      <p class="contact__address">
        <span class="contact__spaced">H A L C Y O N</span><br>
        <span class="contact__spaced">A R C H I T E C T U R E L L C.</span><br>
        4127 NW 52nd Ter. Suite 2308<br>
        Miami, FL 33148
      </p>
      <ul class="contact__lines">
        <li><svg class="icon" viewBox="0 0 12 12"><path d="M1 4c0-2 2-3 3-3l1 2-1 1c0 1 2 3 3 3l1-1 2 1c0 1-1 3-3 3C4 10 1 7 1 4z"/></svg>(305) 555-0184</li>
        <li><svg class="icon" viewBox="0 0 12 12"><path d="M0 2h12v8H0z"/><path d="M1 3l5 3.5L11 3" fill="none" stroke="#fff" stroke-width="1"/></svg><span class="email">mdrummond.halcyongrandestates@mailbox.example</span></li>
        <li><svg class="icon" viewBox="0 0 12 12"><circle cx="6" cy="6" r="5.5"/><path d="M1 6h10M6 1c2 2 2 8 0 10M6 1c-2 2-2 8 0 10" fill="none" stroke="#fff" stroke-width="0.8"/></svg>www.HalcyonGrandEstates.example</li>
      </ul>
    </div>
  </section>

  <section class="card card--back" aria-label="Business card back">
    <div class="back-band" role="img" aria-label="Soft blue gradient field behind the brand name"></div>
    <div class="wordmark wordmark__name">HALCYON</div>
    <div class="wordmark wordmark__sub">ARCHITECTURE LLC</div>
  </section>
</main>
</body>
</html>
```